Business Card Design Project

Keep it simple , using logo and colors that compliment. Logo on one side with complimentary back ground color. Other side, personal info with possible complimentary design/colors

Target Market(s)

we are a non for profit that will be seeking donations . Both monetary and in kind

Industry/Entity Type

Business

Font styles to use
Sans Serif

Colors

Designer to choose colors to be used in the design.

```html
<!DOCTYPE html>
<html lang="en">
<head>
<meta charset="utf-8">
<title>Bright Step Fund – Business Card</title>
<link rel="stylesheet" href="https://fonts.googleapis.com/css2?family=Lato:wght@300;400;700;900&display=swap">
<style>
  :root {
    --backdrop: #2e2e2e;
    --card-white: #ffffff;
    --card-navy: #1f2750;
    --accent-yellow: #e8d800;
    --text-light: #eef0f5;
    --shadow: rgba(0, 0, 0, 0.55);
  }
  html, body {
    margin: 0;
    padding: 0;
    width: 1200px;
    height: 997px;
    overflow: hidden;
    background: var(--backdrop);
  }
  .canvas {
    position: relative;
    width: 1200px;
    height: 997px;
  }
  .card {
    position: absolute;
    width: 560px;
    height: 320px;
    border-radius: 18px;
    overflow: hidden;
    box-shadow: 0 14px 30px var(--shadow);
    background: var(--card-white);
  }
  .card--front { left: 90px; top: 100px; }
  .card--back  { left: 550px; top: 560px; }
  .card svg { display: block; }
  .fill-white  { fill: var(--card-white); }
  .fill-navy   { fill: var(--card-navy); }
  .fill-yellow { fill: var(--accent-yellow); }
  .brand-badge { fill: var(--card-navy); stroke: var(--accent-yellow); stroke-width: 7; }
  .brand-name {
    font-family: "Lato", sans-serif;
    font-weight: 300;
    fill: var(--accent-yellow);
  }
  .person-name {
    font-family: "Lato", sans-serif;
    font-weight: 900;
    font-size: 22px;
    letter-spacing: 0.5px;
    fill: var(--text-light);
  }
  .person-role {
    font-family: "Lato", sans-serif;
    font-weight: 700;
    font-size: 14px;
    fill: var(--accent-yellow);
  }
  .contact-line {
    font-family: "Lato", sans-serif;
    font-weight: 700;
    font-size: 16px;
    fill: var(--text-light);
  }
  .icon-dot { fill: var(--accent-yellow); }
  .icon-glyph { fill: none; stroke: var(--card-navy); stroke-width: 2; stroke-linecap: round; stroke-linejoin: round; }
</style>
</head>
<body>
<main class="canvas">

  <!-- Logo side -->
  <section class="card card--front" aria-label="Business card, logo side">
    <svg width="560" height="320" viewBox="0 0 560 320">
      <rect class="fill-white" width="560" height="320"/>
      <path class="fill-yellow" d="M0,225 C150,150 320,165 560,60 L560,320 L0,320 Z"/>
      <path class="fill-navy" d="M0,247 C160,175 330,185 560,82 L560,320 L0,320 Z"/>
      <circle class="brand-badge" cx="290" cy="160" r="96"/>
      <text class="brand-name" x="290" y="150" font-size="34" text-anchor="middle">Bright Step</text>
      <text class="brand-name" x="290" y="190" font-size="34" text-anchor="middle">Fund</text>
    </svg>
  </section>

  <!-- Contact side -->
  <section class="card card--back" aria-label="Business card, contact side">
    <svg width="560" height="320" viewBox="0 0 560 320">
      <rect class="fill-white" width="560" height="320"/>
      <path class="fill-yellow" d="M0,160 C140,115 300,120 560,100 L560,320 L0,320 Z"/>
      <path class="fill-navy" d="M0,182 C150,138 310,140 560,122 L560,320 L0,320 Z"/>
      <circle class="brand-badge" cx="440" cy="105" r="80"/>
      <text class="brand-name" x="440" y="98" font-size="27" text-anchor="middle">Bright Step</text>
      <text class="brand-name" x="440" y="130" font-size="27" text-anchor="middle">Fund</text>

      <text class="person-name" x="40" y="222">MAREN HOLLOWAY</text>
      <text class="person-role" x="40" y="240">Executive Director</text>

      <!-- phone -->
      <circle class="icon-dot" cx="52" cy="266" r="11"/>
      <rect class="icon-glyph" x="48" y="259" width="8" height="14" rx="1.5"/>
      <text class="contact-line" x="74" y="272">555-204-7718</text>

      <!-- web link -->
      <circle class="icon-dot" cx="52" cy="292" r="11"/>
      <path class="icon-glyph" d="M48,296 L56,288 M46,293 l-1,1 a3,3 0 0 0 4,4 l2,-2 M58,291 l1,-1 a3,3 0 0 0 -4,-4 l-2,2"/>
      <text class="contact-line" x="74" y="298">www.brightstepfund.org</text>

      <!-- email -->
      <circle class="icon-dot" cx="52" cy="316" r="0"/>
      <circle class="icon-dot" cx="300" cy="266" r="11"/>
      <rect class="icon-glyph" x="293" y="261" width="14" height="10" rx="1"/>
      <path class="icon-glyph" d="M293,261 L300,267 L307,261"/>
      <text class="contact-line" x="320" y="272" font-size="14">maren@brightstepfund.org</text>
    </svg>
  </section>

</main>
</body>
</html>
```